Wealth Preservation Book Cover

Our Goals
- The book should attract our target audience
- We give the book (Hardcover and E-Book) directly to selected doctors. Our goal is that they read the book.
- The wealthy personalities become convinced through reading the book and entrust us to manage their wealth
- The cover helps delivering the message of the book. The message is as follows: You can invest your money way better based on evidence (scientific findings). We help you to understand financial markets in a simple way and help you to make wise decisions. Decide how your wealth should be managed in your best interest.

Info:
Our company, called Kornfeld Vermögen AG has a regional lime tree as a logo (www.kornfeldvermoegen.ch). This tree communicates good things: It is big, standing for big wealth, it is steady and old, standing for our long term passive wealth management philosophy. We would like to use this lime tree on the book too. You can find pictures of this tree here of which we are allowed to use in the attachment and on: https://www.facebook.com/brauneiche/?fref=ts

See attachment for booklet including English translation of the cover (for your understanding) for which we are seeking a great job.

Target Market(s)

Our target audience:
Wealthy Doctors in Switzerland with Wealth of CHF/$ 5Mio+
These personalities are usually aged 55+, Wealthy decision makers who believe in evidence and are family oriented and they invest their money for the long term and do not wish to have a lot to do with the finance but want to have a great wealth management solution.

Industry/Entity Type

Asset Management

Colors
0792cd

Requirements
Must have
• Imagine you are a Swiss doctor who owns 5 million dollars.
• Ask yourself: "Is my design good enough that I would entrust it my 5 million?"
Nice to have
• Blue color is often liked by doctors, or at least many medical books use blue color.
• The inside of the book should fit the cover. The message of the cover is positive, life giving.
• For the back maybe a family situation with a strong father, with his attractive wife his daughter and his son, e.g. sitting at a table in a luxurious setting.
• You could use Swiss Mountains for the background.
• Swissness - The setting of the book should be in Switzerland.

```html
<!DOCTYPE html>
<html lang="de">
<head>
<meta charset="utf-8">
<title>Kapital bewahren – Buchcover</title>
<link href="https://fonts.googleapis.com/css2?family=Bebas+Neue&family=Oswald:wght@400;500&display=swap" rel="stylesheet">
<style>
  :root {
    --sky-deep: #1d3656;
    --sky-mid: #3f6a93;
    --sky-light: #8fb0cc;
    --mountain-dark: #1a2a3c;
    --snow: #e9f0f6;
    --white: #ffffff;
    --ink: #111a33;
  }
  html, body {
    margin: 0;
    padding: 0;
    width: 800px;
    height: 1200px;
    overflow: hidden;
    background: var(--white);
  }
  .cover {
    position: relative;
    width: 800px;
    height: 1200px;
    overflow: hidden;
    background: var(--white);
  }
  .cover-photo {
    position: absolute;
    left: 0;
    top: 0;
    width: 800px;
    height: 1018px;
    background:
      linear-gradient(180deg,
        var(--sky-deep) 0%,
        var(--sky-mid) 30%,
        var(--sky-light) 52%,
        #b9cddc 60%,
        #4b6680 70%,
        var(--mountain-dark) 82%,
        #3a5268 90%,
        var(--snow) 100%);
  }
  .title {
    position: absolute;
    left: 0;
    top: 111px;
    width: 800px;
    height: 300px;
    margin: 0;
    text-align: center;
    color: var(--white);
    font-family: "Bebas Neue", "Oswald", sans-serif;
    font-weight: 400;
    line-height: 1;
  }
  .title-line {
    position: absolute;
    left: 0;
    width: 800px;
    display: block;
    font-size: 150px;
    letter-spacing: 1px;
    white-space: nowrap;
  }
  .title-line--first { top: 0; }
  .title-line--second { top: 158px; }
  .subtitle {
    position: absolute;
    left: 0;
    top: 419px;
    width: 800px;
    margin: 0;
    text-align: center;
    color: var(--white);
    font-family: "Bebas Neue", "Oswald", sans-serif;
    font-weight: 400;
    font-size: 63px;
    line-height: 1;
    white-space: nowrap;
  }
  .promise-box {
    position: absolute;
    left: 166px;
    top: 512px;
    width: 468px;
    height: 180px;
    box-sizing: border-box;
    padding: 22px 0 0 20px;
    background: var(--white);
    color: var(--ink);
    font-family: "Oswald", sans-serif;
    font-weight: 500;
    font-size: 25px;
    line-height: 31px;
    white-space: nowrap;
  }
  .promise-box p { margin: 0; }
  .promise-list { list-style: none; margin: 0; padding: 0; }
  .promise-list li::before { content: "• "; }
  .authors {
    position: absolute;
    left: 0;
    top: 1018px;
    width: 800px;
    height: 182px;
    background: var(--white);
    color: var(--ink);
    font-family: "Oswald", sans-serif;
    font-weight: 500;
    font-size: 52px;
    line-height: 64px;
    text-align: center;
    padding-top: 22px;
    box-sizing: border-box;
  }
  .author { display: block; }
</style>
</head>
<body>
  <main class="cover">
    <div class="cover-photo" role="img" aria-label="Verschneite Schweizer Berglandschaft mit Tannen unter blauem Himmel"></div>

    <h1 class="title">
      <span class="title-line title-line--first">Kapital</span>
      <span class="title-line title-line--second">Bewahren</span>
    </h1>
    <p class="subtitle">Wissen und Methode</p>

    <section class="promise-box">
      <p>Lernen Sie</p>
      <ul class="promise-list">
        <li>wie die Wertpapiermärkte funktionieren.</li>
        <li>welche Risiken sich am meisten lohnen.</li>
        <li>wie Sie sicherstellen können, dass in</li>
      </ul>
    </section>

    <footer class="authors">
      <span class="author">Martin R. Steiger</span>
      <span class="author">Dr. med. L. Andreas Wyss</span>
    </footer>
  </main>
</body>
</html>
```